Business Reporting Graph Illustration

I'm looking for a graphic design to created an illustration of a line chart I have two sample charts that I'd like elements of each combined together to create the project. Below is a link to learn more about this project. This should be designed using any product of the Adobe Suite.
Color Scheme is included within the below link. This will require 2 - 3 rounds of design before final completion.

https://www.brovex.com/file/QWTp7ksuHeLM382RK4Vxbd/Graphic-Design-Project

```html
<!DOCTYPE html>
<html lang="en">
<head>
<meta charset="UTF-8">
<title>Business Reporting Line Chart</title>
<link href="https://fonts.googleapis.com/css2?family=Montserrat:wght@400;700&display=swap" rel="stylesheet">
<style>
  :root {
    --navy: #0b1a45;
    --gold: #fbb116;
    --steel: #5b7db5;
    --paper: #ffffff;
  }
  html, body {
    margin: 0;
    padding: 0;
    width: 1200px;
    height: 560px;
    overflow: hidden;
    background: var(--paper);
  }
  .chart {
    display: block;
    width: 1200px;
    height: 560px;
    font-family: "Montserrat", sans-serif;
  }
  .axis-line, .axis-tick { stroke: var(--navy); stroke-width: 1.6; }
  .axis-title { fill: var(--navy); font-size: 19px; font-weight: 400; }
  .axis-label { fill: var(--navy); font-size: 18px; font-weight: 400; text-anchor: middle; }
  .trend-line { fill: none; stroke: var(--gold); stroke-width: 3.3; stroke-linecap: round; stroke-linejoin: round; }
  .event-guide { stroke: var(--steel); stroke-width: 1.5; stroke-dasharray: 4 4; }
  .event-stem { fill: none; stroke: var(--navy); stroke-width: 1.6; }
  .event-ring { fill: var(--steel); }
  .event-dot { fill: var(--navy); }
  .event-tag { fill: var(--navy); }
  .event-text { fill: var(--gold); font-size: 14px; font-weight: 700; text-anchor: middle; dominant-baseline: central; }
</style>
</head>
<body>
<svg class="chart" viewBox="0 0 1200 560" xmlns="http://www.w3.org/2000/svg" role="img" aria-label="Line chart of response over minutes with TV and radio ad markers">

  <!-- guides -->
  <line class="event-guide" x1="479.3" y1="230" x2="479.3" y2="429.6"/>
  <line class="event-guide" x1="770" y1="360" x2="770" y2="429.6"/>
  <line class="event-guide" x1="942.7" y1="419" x2="942.7" y2="429.6"/>

  <!-- trend -->
  <path class="trend-line" d="
    M147.7 410.4
    C162 414 170 420 180.6 431
    C188 438 200 439 215.7 432
    C226 427 232 417 245 414
    C258 412 264 413 280 397
    C295 380 305 360 328.3 348
    C346 340 368 330 384.6 305
    C398 285 402 265 414 244
    C424 226 434 218 450.2 215
    C462 213 472 216 480 222
    C495 234 510 255 535 274
    C555 288 580 292 596 302
    C612 312 624 325 640 340
    C652 350 660 353 671 353
    C686 353 700 347 715 339
    C728 332 735 325 746 327
    C756 329 762 344 772 355
    C780 362 795 362 810 357
    C828 351 836 342 858 338.6
    C874 337 882 346 896 365
    C912 388 925 405 942.7 412
    C952 416 965 416 985 411
    C1005 406 1018 400 1032 401
    C1050 402 1065 408 1079 412
    C1100 418 1118 423 1135 422
    C1150 421 1160 420 1167.8 418.4"/>

  <!-- axis -->
  <line class="axis-line" x1="141.6" y1="429.6" x2="1175" y2="429.6"/>
  <g class="axis-ticks">
    <line class="axis-tick" x1="278.6" y1="429.6" x2="278.6" y2="439.5"/>
    <line class="axis-tick" x1="335.8" y1="429.6" x2="335.8" y2="439.5"/>
    <line class="axis-tick" x1="393" y1="429.6" x2="393" y2="439.5"/>
    <line class="axis-tick" x1="450.7" y1="429.6" x2="450.7" y2="439.5"/>
    <line class="axis-tick" x1="508" y1="429.6" x2="508" y2="439.5"/>
    <line class="axis-tick" x1="565.6" y1="429.6" x2="565.6" y2="439.5"/>
    <line class="axis-tick" x1="622.8" y1="429.6" x2="622.8" y2="439.5"/>
    <line class="axis-tick" x1="680.5" y1="429.6" x2="680.5" y2="439.5"/>
    <line class="axis-tick" x1="737.7" y1="429.6" x2="737.7" y2="439.5"/>
    <line class="axis-tick" x1="795" y1="429.6" x2="795" y2="439.5"/>
    <line class="axis-tick" x1="852.6" y1="429.6" x2="852.6" y2="439.5"/>
    <line class="axis-tick" x1="909.9" y1="429.6" x2="909.9" y2="439.5"/>
    <line class="axis-tick" x1="967" y1="429.6" x2="967" y2="439.5"/>
    <line class="axis-tick" x1="1024.8" y1="429.6" x2="1024.8" y2="439.5"/>
    <line class="axis-tick" x1="1082" y1="429.6" x2="1082" y2="439.5"/>
  </g>
  <text class="axis-title" x="48" y="436">MINUTES</text>
  <g class="axis-labels">
    <text class="axis-label" x="252" y="456">1</text>
    <text class="axis-label" x="312" y="456">2</text>
    <text class="axis-label" x="369" y="456">3</text>
    <text class="axis-label" x="428" y="456">4</text>
    <text class="axis-label" x="484.5" y="456">5</text>
    <text class="axis-label" x="541.7" y="456">6</text>
    <text class="axis-label" x="599" y="456">7</text>
    <text class="axis-label" x="656.6" y="456">8</text>
    <text class="axis-label" x="713.8" y="456">9</text>
    <text class="axis-label" x="774.8" y="456">10</text>
    <text class="axis-label" x="830" y="456">11</text>
    <text class="axis-label" x="888.8" y="456">12</text>
    <text class="axis-label" x="946.4" y="456">13</text>
    <text class="axis-label" x="1004.6" y="456">14</text>
    <text class="axis-label" x="1061" y="456">15</text>
  </g>

  <!-- event: TV ad at minute 5 -->
  <g class="event">
    <path class="event-stem" d="M479.3 221 V158.8 Q479.3 154.8 483.3 154.8 H500"/>
    <rect class="event-tag" x="498" y="143.5" width="86" height="22.5" rx="11.25"/>
    <text class="event-text" x="541" y="154.8">TV Ad</text>
    <circle class="event-ring" cx="479.3" cy="221.4" r="10.3"/>
    <circle class="event-dot" cx="479.3" cy="221.4" r="7.5"/>
  </g>

  <!-- event: TV ad at minute 10 -->
  <g class="event">
    <path class="event-stem" d="M770 351 V288.7 Q770 284.7 774 284.7 H791"/>
    <rect class="event-tag" x="789" y="273.4" width="86" height="22.6" rx="11.3"/>
    <text class="event-text" x="832" y="284.7">TV Ad</text>
    <circle class="event-ring" cx="770" cy="351.3" r="10.3"/>
    <circle class="event-dot" cx="770" cy="351.3" r="7.5"/>
  </g>

  <!-- event: radio ad at minute 13 -->
  <g class="event">
    <path class="event-stem" d="M942.7 410 V374.5 Q942.7 370.5 946.7 370.5 H963"/>
    <rect class="event-tag" x="961.5" y="359.3" width="85.8" height="22" rx="11"/>
    <text class="event-text" x="1004.4" y="370.3">Radio Ad</text>
    <circle class="event-ring" cx="942.7" cy="410.4" r="10.3"/>
    <circle class="event-dot" cx="942.7" cy="410.4" r="7.5"/>
  </g>
</svg>
</body>
</html>
```